Business Card Design

I need a business card design for a photography business that specializes in headshots and portraits.

Target Market(s)

Business professionals, actors, actresses

Industry/Entity Type

Business

Contact Information for Business Card

Cobalt Ridge Photography, Greg Whitlow, 5817 Kellerman Ave, Suite 416, Fort Wayne, IN 46915, 260.555.0187, www.cobaltridgephoto.example. greg.whitlow@cobaltridgephoto.example

Requirements
Must have
• The business card should state the type of photography services offered: headshots and portraits.

```html
<!DOCTYPE html>
<html lang="en">
<head>
<meta charset="utf-8">
<title>Cobalt Ridge Photography — Business Card</title>
<link rel="stylesheet" href="https://fonts.googleapis.com/css2?family=Marcellus+SC&family=Open+Sans:wght@400&display=swap">
<style>
  :root {
    --page: #141414;
    --card-black: #0b0b0b;
    --card-carbon: #1c1c1c;
    --accent: #f2dc1c;
    --accent-deep: #d9c010;
    --text-light: #e6e6e6;
    --text-dark: #111111;
  }
  html, body {
    margin: 0;
    width: 1200px;
    height: 900px;
    overflow: hidden;
    background: var(--page);
  }
  .business-card {
    position: absolute;
    left: 145px;
    top: 190px;
    width: 910px;
    height: 520px;
    border-radius: 30px;
    overflow: hidden;
    background: radial-gradient(ellipse at 60% 55%, var(--card-carbon), var(--card-black) 80%);
    box-shadow: 0 0 0 7px var(--accent);
  }
  .card-shapes {
    position: absolute;
    inset: 0;
  }
  .brand-name {
    position: absolute;
    left: 368px;
    top: 86px;
    margin: 0;
    font-family: "Marcellus SC", serif;
    font-size: 24px;
    line-height: 1.2;
    font-weight: 400;
    color: var(--accent);
    white-space: nowrap;
  }
  .contact-block {
    position: absolute;
    right: 58px;
    top: 150px;
    text-align: right;
    font-family: "Open Sans", sans-serif;
    color: var(--text-light);
  }
  .studio-name,
  .photographer-name {
    font-family: "Marcellus SC", serif;
    color: var(--accent);
    margin: 0;
    font-weight: 400;
  }
  .studio-name { font-size: 30px; line-height: 1.2; }
  .photographer-name { font-size: 26px; line-height: 1.2; margin-bottom: 22px; }
  .address { font-size: 20px; line-height: 1.3; margin: 0 0 20px; font-style: normal; }
  .contact-list { list-style: none; margin: 0; padding: 0; font-size: 20px; line-height: 1.55; }
  .contact-list li { display: flex; align-items: center; justify-content: flex-end; gap: 12px; }
  .contact-icon {
    width: 22px; height: 22px; flex: none;
    border-radius: 4px;
  }
  .tagline {
    position: absolute;
    right: 58px;
    bottom: 24px;
    margin: 0;
    font-family: "Marcellus SC", serif;
    font-size: 26px;
    color: var(--accent);
  }
</style>
</head>
<body>
  <section class="business-card">
    <svg class="card-shapes" width="910" height="520" viewBox="0 0 910 520" aria-hidden="true">
      <polygon class="top-band" points="380,0 910,0 910,40 540,40 455,78 395,78" fill="var(--accent)"/>
      <polygon class="left-wing" points="0,112 228,112 262,150 0,150" fill="var(--accent)"/>
      <polygon class="left-wing-lower" points="0,162 240,162 272,186 0,186" fill="var(--accent-deep)"/>
      <circle class="brand-dot" cx="312" cy="100" r="42" fill="var(--accent)"/>
    </svg>

    <p class="brand-name">Cobalt Ridge Photography</p>

    <div class="contact-block">
      <h1 class="studio-name">Cobalt Ridge Photography</h1>
      <h2 class="photographer-name">Greg Whitlow</h2>
      <address class="address">5817 Kellerman Ave, Suite 416<br>Fort Wayne, IN 46915</address>
      <ul class="contact-list">
        <li>260.555.0187 <svg class="contact-icon" viewBox="0 0 22 22" aria-label="phone"><rect width="22" height="22" rx="4" fill="var(--accent)"/><path d="M7 5l3 3-1.5 1.5c1 2 2 3 4 4L14 12l3 3-2 2c-5 0-10-5-10-10z" fill="var(--text-dark)"/></svg></li>
        <li>www.cobaltridgephoto.example <svg class="contact-icon" viewBox="0 0 22 22" aria-label="website"><rect width="22" height="22" rx="4" fill="var(--accent)"/><circle cx="11" cy="11" r="6" fill="none" stroke="var(--text-dark)" stroke-width="1.6"/><line x1="5" y1="11" x2="17" y2="11" stroke="var(--text-dark)" stroke-width="1.4"/></svg></li>
        <li>greg.whitlow@cobaltridgephoto.example <svg class="contact-icon" viewBox="0 0 22 22" aria-label="email"><rect width="22" height="22" rx="4" fill="var(--accent)"/><rect x="4.5" y="6.5" width="13" height="9" fill="none" stroke="var(--text-dark)" stroke-width="1.5"/><path d="M4.5 6.5l6.5 5 6.5-5" fill="none" stroke="var(--text-dark)" stroke-width="1.5"/></svg></li>
      </ul>
    </div>

    <p class="tagline">specializes in headshots and portraits</p>
  </section>
</body>
</html>
```